Business card design needed

We would like a new design for our window furnishings & home decor business. We supply & install blinds, curtains, shutters etc. We are about to incorporate home decor products like cushoins & throws...
We'd like to use moderns browns & green tones. Casual but elegant style. Maybe textured/patterned look design. Design should communicate quality and great value with latest designs.

website & FB page & email is still to be advised so pls provide space.

Industry/Entity Type

Business

Contact Information for Business Card

Marlowe Haven
Window Furnishings & Home Decor
Genevieve - Interior Stylist
Call us now for a free measure & quote - 63124089
0412 906 358
0418 273 564

```html
<!DOCTYPE html>
<html lang="en">
<head>
<meta charset="utf-8">
<title>Marlowe Haven – Business Card</title>
<link href="https://fonts.googleapis.com/css2?family=Indie+Flower&display=swap" rel="stylesheet">
<style>
  :root {
    --page-bg: #e9eaee;
    --card-green: #9fd063;
    --band-green: #a9d56d;
    --text-brown: #4f2410;
    --pattern-gold: #b0913f;
    --pattern-olive: #8c7a2e;
    --pattern-tan: #c3a45a;
    --pattern-rust: #a8743a;
    --card-shadow: rgba(40, 40, 60, 0.18);
  }
  * { box-sizing: border-box; margin: 0; padding: 0; }
  html, body {
    width: 1200px;
    height: 796px;
    overflow: hidden;
    background: var(--page-bg);
    font-family: "Indie Flower", cursive;
    color: var(--text-brown);
  }
  .canvas {
    width: 1200px;
    height: 796px;
    display: flex;
    align-items: center;
    justify-content: center;
    gap: 60px;
  }
  .card {
    width: 525px;
    height: 300px;
    position: relative;
    overflow: hidden;
    box-shadow: 0 8px 22px var(--card-shadow);
  }
  .card-front { background: var(--pattern-gold); }
  .pattern-area {
    position: absolute;
    left: 0;
    width: 100%;
    background:
      radial-gradient(ellipse at 30% 40%, rgba(195, 164, 90, 0.6), transparent 60%),
      linear-gradient(135deg, var(--pattern-tan), var(--pattern-gold) 45%, var(--pattern-rust) 70%, var(--pattern-olive));
  }
  .pattern-top { top: 0; height: 128px; }
  .pattern-bottom { bottom: 0; height: 128px; }
  .name-band {
    position: absolute;
    top: 128px;
    left: 0;
    width: 100%;
    height: 44px;
    background: var(--band-green);
    display: flex;
    align-items: center;
    justify-content: center;
    padding: 0 16px;
  }
  .business-line {
    font-size: 14px;
    white-space: nowrap;
    letter-spacing: 0.1px;
  }
  .card-back { background: var(--card-green); }
  .call-line {
    position: absolute;
    top: 112px;
    left: 44px;
    font-size: 26px;
  }
  .phone-row {
    position: absolute;
    top: 168px;
    left: 44px;
    right: 44px;
    display: flex;
    justify-content: space-between;
    font-size: 22px;
  }
</style>
</head>
<body>
  <main class="canvas">
    <section class="card card-front" aria-label="Card front">
      <div class="pattern-area pattern-top" role="img" aria-label="Decorative pattern of circles and crosses in golden brown tones"></div>
      <div class="name-band">
        <span class="business-line">Marlowe Haven Window Furnishings &amp; Home Decor Genevieve - Interior Stylist</span>
      </div>
      <div class="pattern-area pattern-bottom" role="img" aria-label="Decorative pattern of circles and crosses in golden brown tones"></div>
    </section>
    <section class="card card-back" aria-label="Card back">
      <p class="call-line">Call us now for a free measure &amp; quote</p>
      <div class="phone-row">
        <span class="phone">63124089</span>
        <span class="phone">0412 906 358</span>
        <span class="phone">0418 273 564</span>
      </div>
    </section>
  </main>
</body>
</html>
```